Packaging box design (uLumo style)

To create a striking but minimalist box for a new tool handle. The top sleeve external box dimensions are L230xW85xH65mm. We will need the logo (plia by KVR), you can use any of our rendered drawings if you feel it would look good. Information to be included; Ergonomic Adjustable Handle / 12 position lock system / Quick release shaft / Weight and space saving / Comfort grip / Ability to convert existing toolsFor purchase and converting options please visit (USA) www.brasolmark.com or (Europe) www.kvrtools.com.

Target Market(s)

Automotive professionals

Font styles to use
Sans Serif

Colors
fbed22
333333
5c5c5c
9d9d9d

Requirements
Must have
• Logo - plia by KVR (attached)

```html
<!DOCTYPE html>
<html lang="en">
<head>
<meta charset="utf-8">
<title>plia series by KVR – handle box</title>
<link href="https://fonts.googleapis.com/css2?family=Lato:wght@400;700;900&display=swap" rel="stylesheet">
<style>
  :root {
    --yellow: #e2d81f;
    --charcoal: #333333;
    --graphite: #2b2b2b;
    --mid-grey: #5c5c5c;
    --light-grey: #9d9d9d;
    --backdrop: #e4e5e7;
    --white: #ffffff;
    --product-gold: #c9b46a;
  }
  * { margin: 0; padding: 0; box-sizing: border-box; }
  html, body { width: 1200px; height: 900px; overflow: hidden; }
  body {
    background: var(--backdrop);
    font-family: "Lato", sans-serif;
    position: relative;
  }
  .dieline { position: absolute; left: 33px; top: 180px; width: 1134px; height: 540px; }

  .panel { position: absolute; overflow: hidden; }
  .panel--top { left: 0; top: 0; width: 828px; height: 306px; background: var(--charcoal); }
  .panel--front { left: 0; top: 306px; width: 828px; height: 234px; background: var(--yellow); }
  .panel--end { left: 828px; top: 306px; width: 306px; height: 234px; background: var(--yellow); }

  .handle-drawing {
    position: absolute; left: 230px; top: 40px; width: 560px; height: 220px;
    background: linear-gradient(90deg, #3a3a3a, #444 60%, #3d3d3d);
    border-radius: 110px 110px 110px 110px / 110px 110px 110px 110px;
  }

  .logo { position: absolute; line-height: 1; }
  .logo__word { display: block; font-weight: 900; letter-spacing: -1px; }
  .logo__sub { display: block; font-weight: 700; }
  .logo__sub small { font-size: 0.6em; font-weight: 700; }

  .logo--top { left: 40px; top: 200px; color: var(--white); }
  .logo--top .logo__word { font-size: 58px; }
  .logo--top .logo__sub { font-size: 22px; margin-left: 18px; }

  .logo--front-left { left: 28px; top: 80px; color: var(--graphite); }
  .logo--front-left .logo__word { font-size: 50px; }
  .logo--front-left .logo__sub { font-size: 19px; margin-left: 16px; }

  .logo--front-right { left: 640px; top: 140px; color: var(--graphite); }
  .logo--front-right .logo__word { font-size: 46px; }
  .logo--front-right .logo__sub { font-size: 18px; margin-left: 14px; }

  .logo--end { left: 60px; top: 80px; color: var(--graphite); }
  .logo--end .logo__word { font-size: 62px; }
  .logo--end .logo__sub { font-size: 22px; margin-left: 20px; }

  .product-render {
    position: absolute; left: 180px; top: 0; width: 270px; height: 234px;
    background: radial-gradient(ellipse at 40% 40%, #d9c784, var(--product-gold) 55%, #8d7d45);
    border-radius: 0 140px 120px 0;
  }

  .thumb-notch {
    position: absolute; left: 414px; top: -1px; transform: translateX(-50%);
    width: 56px; height: 28px; border-radius: 0 0 28px 28px; background: var(--backdrop);
  }

  .feature-list { position: absolute; left: 500px; top: 22px; list-style: none; color: var(--graphite); }
  .feature-list li { font-size: 13px; line-height: 17px; padding-left: 10px; position: relative; }
  .feature-list li::before {
    content: ""; position: absolute; left: 0; top: 8px; width: 5px; height: 1px; background: var(--mid-grey);
  }
  .feature-list .feature--key { font-weight: 700; font-size: 14px; }
  .feature-list .feature--minor { color: var(--mid-grey); }
</style>
</head>
<body>
  <main class="dieline">
    <section class="panel panel--top">
      <div class="handle-drawing" role="img" aria-label="Line drawing of the adjustable handle, top view"></div>
      <div class="logo logo--top">
        <span class="logo__word">plia</span>
        <span class="logo__sub">series <small>by</small>KVR</span>
      </div>
    </section>

    <section class="panel panel--front">
      <div class="thumb-notch"></div>
      <div class="logo logo--front-left">
        <span class="logo__word">plia</span>
        <span class="logo__sub">series <small>by</small>KVR</span>
      </div>
      <div class="product-render" role="img" aria-label="Rendered photo of the gold handle with black grip inserts"></div>
      <ul class="feature-list">
        <li class="feature--key">Ergonomic Adjustable Handle</li>
        <li class="feature--minor">12 position lock system</li>
        <li class="feature--key">Quick release shaft</li>
        <li class="feature--minor">Weight and space saving</li>
        <li class="feature--key">Comfort grip</li>
        <li class="feature--minor">Ability to convert existing tools</li>
      </ul>
      <div class="logo logo--front-right">
        <span class="logo__word">plia</span>
        <span class="logo__sub">series <small>by</small>KVR</span>
      </div>
    </section>

    <section class="panel panel--end">
      <div class="logo logo--end">
        <span class="logo__word">plia</span>
        <span class="logo__sub">series <small>by</small>KVR</span>
      </div>
    </section>
  </main>
</body>
</html>
```